Wine Label for Tallowick Vineyards

I grow my own grapes and make my own wine. I do this just as a hobby and do not sell any wine. I just make it for my own use and to give as gifts. I still endeavor to make the bottle look like a genuine retail bottle, so I need a professional looking label.

Brindle Knob is a state park in North Carolina. My vineyard is at the base of the mountain. Tallowick is the name the Indians called the mountain. It means "great guide" as they used the mountain as a landmark in their travels.

Need front and back label. Attached is a picture that I currently use. The new labels should contain all the language on the current label.

Size of label flexible as long as it is a standard size label, that can be easily found.

I think Brindle Knob image should be included, maybe stylized. I am looking for something for earthy, rustic and clean.

The varieties will be Pinot Noir, Cabernet Sauvignon, Carbernet Franc, Chardonnay, and Viognier. I guess all the labels would be the same, just the name would change, Unless someone has a better idea.

Target Market(s)

wine drinker

Requirements
Must have
• brindle knob image of some sort,
• front and back label
Nice to have
• Clean, earthy, rustic - the label should feel like the mountain look, even romantic

```html
<!DOCTYPE html>
<html lang="en">
<head>
<meta charset="utf-8">
<title>Tallowick Vineyards – Cabernet Sauvignon Label</title>
<link href="https://fonts.googleapis.com/css2?family=Cormorant+Garamond:wght@400;500&family=Pinyon+Script&display=swap" rel="stylesheet">
<style>
  :root {
    --paper: #e6e6e5;
    --ink: #111111;
    --maroon: #3a2224;
    --gold: #cdb46a;
    --gold-deep: #c2a85c;
  }
  html, body {
    margin: 0;
    padding: 0;
    width: 1200px;
    height: 1200px;
    overflow: hidden;
    background: var(--paper);
  }
  .label {
    position: relative;
    width: 1200px;
    height: 1200px;
    overflow: hidden;
    background: linear-gradient(135deg, #dcdcdb 0%, #ececeb 45%, #e2e2e1 100%);
    color: var(--ink);
  }
  .tilt {
    position: absolute;
    transform-origin: 0 0;
    transform: rotate(47deg);
    white-space: nowrap;
    line-height: 1;
  }
  .brand-name {
    left: 520px;
    top: -660px;
    font-family: "Cormorant Garamond", serif;
    font-weight: 500;
    font-size: 190px;
    letter-spacing: 14px;
    color: var(--ink);
  }
  .brand-sub {
    left: 768px;
    top: 6px;
    font-family: "Cormorant Garamond", serif;
    font-weight: 500;
    font-size: 84px;
    letter-spacing: 10px;
    color: var(--maroon);
  }
  .variety {
    left: 240px;
    top: 40px;
    font-family: "Pinyon Script", cursive;
    font-size: 118px;
    letter-spacing: 14px;
    color: var(--ink);
  }
  .vintage-caption {
    left: 455px;
    top: 528px;
    display: flex;
    align-items: center;
    gap: 28px;
    font-family: "Cormorant Garamond", serif;
    font-size: 24px;
    letter-spacing: 8px;
  }
  .vintage-caption .rule {
    display: block;
    width: 90px;
    height: 2px;
    background: var(--ink);
  }
  .vintage {
    left: 280px;
    top: 520px;
    font-family: "Cormorant Garamond", serif;
    font-weight: 400;
    font-size: 290px;
    letter-spacing: 24px;
  }
  .origin-band {
    left: -140px;
    top: 560px;
    width: 1500px;
    height: 104px;
    background: linear-gradient(180deg, var(--gold) 0%, var(--gold-deep) 100%);
    display: flex;
    align-items: center;
    font-family: "Cormorant Garamond", serif;
    font-weight: 500;
    font-size: 70px;
    letter-spacing: 4px;
    color: var(--ink);
    padding-left: 40px;
    box-sizing: border-box;
  }
  .bottler {
    left: -90px;
    top: 930px;
    font-family: "Cormorant Garamond", serif;
    font-size: 62px;
    letter-spacing: 6px;
    color: var(--ink);
  }
</style>
</head>
<body>
  <main class="label">
    <div class="tilt brand-name">TALLOWICK</div>
    <div class="tilt brand-sub">VINEYARDS</div>
    <div class="tilt variety">Cabernet Sauvignon</div>
    <div class="tilt vintage-caption"><span class="rule"></span><span>YEAR</span><span class="rule"></span></div>
    <div class="tilt vintage">2015</div>
    <div class="tilt origin-band">PRODUCT OF USA - NORTH CAROLINA</div>
    <div class="tilt bottler">BOTTLED BY TALLOWICK VINEYARDS</div>
  </main>
</body>
</html>
```